out of the box Business Card Design for a Manufacturer / Distributor

We are a manufarturer and distributor of products.
the company name is VORTANI (Pic attached)

the picture is NOT a must have on the business Card.

the Business Card should look really professional and/or special, so out of the box thinking is welcome.

there should be 2 Adresses on the Business Card for Main and Branch Office.
Email Adress, homepage, Name is required
NO Phone Number

Our working field:
Private Labeling
high Quality Production
direct distribution
warehousing
trademark registration
legal support

Main Office:
Kornblumenweg 14
08352 Auenstedt
Germany

Branch Office:
Daska Lane
Rahimpur
Pakistan

Names:
Lukas Feldhaus (Owner)
Imran Qureshi (Owner)

Email:
lukas@vortani-example.com
imran@vortani-example.com

homepage:
vortani-example.com

Industry/Entity Type

Manufacturer Distributer

Contact Information for Business Card

Vortani

Requirements
Must have
• Names, both office Adresses, email, homepage
Should not have
• Phone Number

```html
<!DOCTYPE html>
<html lang="en">
<head>
<meta charset="utf-8">
<title>Vortani Business Card</title>
<link rel="stylesheet" href="https://fonts.googleapis.com/css2?family=Arimo:wght@400;700&family=Nunito+Sans:wght@400&display=swap">
<style>
  :root {
    --orange: #e6a229;
    --panel: #4b4b4b;
    --panel-dark: #3e3e3e;
    --card-dark: #424242;
    --divider: #5a5a5a;
    --white: #ffffff;
    --bg-light: #ffffff;
    --bg-dark: #6f7072;
  }
  html, body {
    margin: 0;
    padding: 0;
    width: 1200px;
    height: 1200px;
    overflow: hidden;
  }
  body {
    background: radial-gradient(circle at 50% 50%, var(--bg-light) 0%, #b9babb 38%, var(--bg-dark) 75%);
  }
  .canvas { display: block; width: 1200px; height: 1200px; }
  .wordmark { font-family: "Nunito Sans", sans-serif; fill: var(--white); }
  .body-text { font-family: "Arimo", sans-serif; fill: var(--white); }
  .service { font-size: 14px; }
  .web { font-size: 13.5px; }
  .person { font-size: 16px; font-weight: 700; }
  .role { font-size: 14px; }
  .office-title { font-size: 11px; font-weight: 700; text-decoration: underline; }
  .office-line { font-size: 11px; }
  .email { font-size: 12px; }
  .bullet { fill: var(--orange); }
  .panel { fill: var(--panel); }
  .panel-center { fill: var(--panel-dark); }
  .divider { stroke: var(--divider); stroke-width: 1; }
  .icon-disc { fill: var(--white); }
  .icon-glyph { fill: var(--panel-dark); }
</style>
</head>
<body>
<svg class="canvas" viewBox="0 0 825 825" xmlns="http://www.w3.org/2000/svg">
  <defs>
    <filter id="wave-shadow" x="-10%" y="-30%" width="120%" height="160%">
      <feDropShadow dx="0" dy="-3" stdDeviation="5" flood-color="#000" flood-opacity="0.45"/>
    </filter>
    <clipPath id="front-wave">
      <path d="M138,265 C198,234 238,213 280,213 C338,213 368,255 420,255 C472,255 502,213 560,213 C602,213 643,234 703,265 V393 H138 Z"/>
    </clipPath>
    <clipPath id="back-wave">
      <path d="M137,625 C190,600 220,572 262,572 C320,572 360,612 420,612 C480,612 520,575 570,575 C620,575 660,600 702,625 V751 H137 Z"/>
    </clipPath>
  </defs>

  <g class="card card-front">
    <rect x="138" y="84" width="565" height="309" fill="var(--orange)"/>
    <path filter="url(#wave-shadow)" fill="var(--panel)" d="M138,265 C198,234 238,213 280,213 C338,213 368,255 420,255 C472,255 502,213 560,213 C602,213 643,234 703,265 V393 H138 Z"/>
    <g clip-path="url(#front-wave)">
      <rect class="panel" x="138" y="200" width="189" height="193"/>
      <rect class="panel-center" x="327" y="200" width="186" height="193"/>
      <rect class="panel" x="513" y="200" width="190" height="193"/>
      <line class="divider" x1="327" y1="200" x2="327" y2="393"/>
      <line class="divider" x1="513" y1="200" x2="513" y2="393"/>
    </g>

    <g class="brand">
      <circle cx="331" cy="168" r="15" fill="var(--white)"/>
      <text class="wordmark" x="354" y="181" font-size="35">VORTANI</text>
    </g>

    <g class="services services-left body-text">
      <circle class="bullet" cx="156" cy="321" r="4"/>
      <text class="service" x="167" y="327">Private Labeling</text>
      <circle class="bullet" cx="156" cy="339" r="4"/>
      <text class="service" x="167" y="345">High Quality Production</text>
      <circle class="bullet" cx="156" cy="357" r="4"/>
      <text class="service" x="167" y="363">Direct Distribution</text>
    </g>

    <g class="website">
      <g fill="none" stroke="var(--white)" stroke-width="1.4">
        <circle cx="420" cy="321" r="13"/>
        <ellipse cx="420" cy="321" rx="6" ry="13"/>
        <line x1="407" y1="321" x2="433" y2="321"/>
        <path d="M409,314 H431 M409,328 H431"/>
        <line x1="420" y1="308" x2="420" y2="334"/>
      </g>
      <text class="body-text web" x="420" y="356" text-anchor="middle">www.vortani-example.com</text>
    </g>

    <g class="services services-right body-text">
      <circle class="bullet" cx="529" cy="321" r="4"/>
      <text class="service" x="540" y="327">Warehousing</text>
      <circle class="bullet" cx="529" cy="339" r="4"/>
      <text class="service" x="540" y="345">Trademark Registration</text>
      <circle class="bullet" cx="529" cy="357" r="4"/>
      <text class="service" x="540" y="363">Legal Support</text>
    </g>
  </g>

  <g class="card card-back">
    <rect x="137" y="442" width="565" height="309" fill="var(--card-dark)"/>
    <path filter="url(#wave-shadow)" class="panel" d="M137,625 C190,600 220,572 262,572 C320,572 360,612 420,612 C480,612 520,575 570,575 C620,575 660,600 702,625 V751 H137 Z"/>
    <g clip-path="url(#back-wave)">
      <rect class="panel" x="137" y="560" width="190" height="191"/>
      <rect class="panel-center" x="327" y="560" width="186" height="191"/>
      <rect class="panel" x="513" y="560" width="189" height="191"/>
      <line class="divider" x1="327" y1="560" x2="327" y2="751"/>
      <line class="divider" x1="513" y1="560" x2="513" y2="751"/>
    </g>

    <g class="people body-text">
      <text class="person" x="161" y="505">Lukas Feldhaus</text>
      <text class="role" x="300" y="506">Owner</text>
      <text class="person" x="161" y="525">Imran Qureshi</text>
      <text class="role" x="300" y="525">Owner</text>
    </g>

    <g class="brand">
      <circle cx="551" cy="500" r="11" fill="var(--white)"/>
      <text class="wordmark" x="570" y="509" font-size="25">VORTANI</text>
    </g>

    <g class="office office-main body-text" text-anchor="middle">
      <circle class="icon-disc" cx="231" cy="654" r="12"/>
      <path class="icon-glyph" d="M231,646 L239,653 H237 V661 H233 V656 H229 V661 H225 V653 H223 Z"/>
      <text class="office-title" x="231" y="685">Main Office:</text>
      <text class="office-line" x="231" y="699">Kornblumenweg 14</text>
      <text class="office-line" x="231" y="714">08352 Auenstedt</text>
      <text class="office-line" x="231" y="729">Germany</text>
    </g>

    <g class="contact-email body-text" text-anchor="middle">
      <circle class="icon-disc" cx="419" cy="654" r="12"/>
      <path class="icon-glyph" d="M411,652 L427,646 L421,662 L418,656 Z"/>
      <text class="email" x="419" y="699">lukas@vortani-example.com</text>
      <text class="email" x="419" y="713">imran@vortani-example.com</text>
    </g>

    <g class="office office-branch body-text" text-anchor="middle">
      <circle class="icon-disc" cx="603" cy="654" r="12"/>
      <path class="icon-glyph" d="M603,646 L611,653 H609 V661 H605 V656 H601 V661 H597 V653 H595 Z"/>
      <text class="office-title" x="603" y="685">Branch Office:</text>
      <text class="office-line" x="603" y="699">Daska Lane</text>
      <text class="office-line" x="603" y="714">Rahimpur</text>
      <text class="office-line" x="603" y="729">Pakistan</text>
    </g>
  </g>
</svg>
</body>
</html>
```